Digital Menu for New Picnic Company

We're in the process of creating a new picnic business called Cedar Hollow Hampers. We need our menu created as per the content in this google doc https://files.examplecloud.net/doc/7Kq2Rv9LmTzX4bWcYhJnPaE3sUd8FgVoNiQ5rMtLyKe/view?share=link
Please look at our website www.cedarhollowhampers.com.au to get an understanding of what we do and our branding style. We need the menu to be created matching the branding/colours as per our website however other than that please feel free to design it however you like and I will provide feedback from there. We are offering a high end gourmet product so the look and feel of the menu does need to reflect this.
PLEASE NOTE: This menu will only be displayed online as a PDF and doesn't need to be printed or provided physically.

```html
<!DOCTYPE html>
<html lang="en">
<head>
<meta charset="utf-8">
<title>Cedar Hollow Hampers — Menu</title>
<link rel="stylesheet" href="https://fonts.googleapis.com/css2?family=Arvo:wght@400;700&family=Kreon:wght@400&family=Lato:wght@900&display=swap">
<style>
  :root {
    --brand-blue: #0a9de2;
    --panel-light: #62c2ef;
    --panel-mid: #4db8eb;
    --white: #ffffff;
    --page: #ffffff;
  }
  * { box-sizing: border-box; }
  html, body {
    margin: 0;
    width: 887px;
    height: 1200px;
    overflow: hidden;
    background: var(--page);
  }
  .menu {
    position: relative;
    width: 887px;
    height: 1200px;
    background: var(--page);
    font-family: "Arvo", serif;
    color: var(--white);
  }

  /* Header */
  .brand-mark {
    position: absolute;
    left: 203px; top: 18px;
    width: 164px; height: 164px;
    border-radius: 50%;
    background: var(--brand-blue);
    display: flex; align-items: center; justify-content: center;
    text-align: center;
  }
  .brand-name {
    margin: 0;
    font: 700 17px/1.2 "Arvo", serif;
    color: var(--white);
  }
  .menu-title {
    position: absolute;
    left: 384px; top: 52px;
    margin: 0;
    font: 700 92px/1 "Arvo", serif;
    color: var(--brand-blue);
    letter-spacing: 1px;
  }

  /* Section panels */
  .section {
    position: absolute;
    left: 27px; width: 833px;
    border-radius: 30px;
  }
  .section--cheese { top: 215px; height: 240px; background: var(--panel-light); }
  .section--crackers { top: 516px; height: 234px; background: var(--panel-mid); }
  .section--fruit { top: 809px; height: 371px; background: var(--panel-mid); }

  .section-tab {
    position: absolute;
    height: 44px;
    border-radius: 22px;
    background: var(--brand-blue);
    border: 4px solid var(--white);
    display: flex; align-items: center; justify-content: center;
    font: 700 19px/1 "Arvo", serif;
    color: var(--white);
    margin: 0;
  }
  .section-tab--cheese { left: 337px; top: 192px; width: 214px; }
  .section-tab--crackers { left: 361px; top: 493px; width: 164px; }
  .section-tab--fruit { left: 380px; top: 786px; width: 129px; }

  /* Photo placeholders */
  .photo {
    position: absolute;
    width: 140px; height: 140px;
    border-radius: 50%;
  }
  .photo--blue-vein { left: 66px; top: 263px; background: radial-gradient(circle at 55% 45%, #ece6d6 0%, #bfb9a6 45%, #6f7466 100%); }
  .photo--salsa { left: 478px; top: 263px; background: radial-gradient(circle at 50% 45%, #c42a18 0%, #b33020 38%, #f4f1ec 44%, #e8dcc4 100%); }
  .photo--artisan { left: 66px; top: 564px; background: radial-gradient(circle at 50% 45%, #7a6448 0%, #8a6040 50%, #3e3226 100%); }
  .photo--rice { left: 478px; top: 564px; background: radial-gradient(circle at 50% 50%, #e07b2e 0%, #e59a52 55%, #fbf3ea 100%); }
  .photo--strawberry { left: 66px; top: 857px; background: radial-gradient(circle at 50% 55%, #d01f27 0%, #a8182a 50%, #5a3230 100%); }
  .photo--grapes { left: 478px; top: 857px; background: radial-gradient(circle at 50% 45%, #b7cc6c 0%, #8f9a5a 45%, #6a5240 100%); }
  .photo--kiwi { left: 266px; top: 1023px; background: radial-gradient(circle at 55% 50%, #7fb03a 0%, #a08850 45%, #6a5230 100%); }

  /* Menu items */
  .item { position: absolute; }
  .item-name {
    margin: 0;
    padding-left: 6px;
    font: 400 38px/40px "Kreon", serif;
    white-space: nowrap;
  }
  .item-name--stacked {
    font-size: 34px;
    line-height: 26px;
    text-align: center;
    padding-left: 0;
  }
  .item-name--centered { text-align: center; padding-left: 0; }
  .rule {
    position: relative;
    height: 2px;
    margin: 4px 4px 0;
    background: var(--white);
  }
  .rule::before, .rule::after {
    content: "";
    position: absolute;
    top: -3px;
    width: 8px; height: 8px;
    border: 1.5px solid var(--white);
    border-radius: 50%;
    background: transparent;
  }
  .rule::before { left: -6px; }
  .rule::after { right: -6px; }
  .rule-tick {
    position: absolute;
    left: 50%; top: -4px;
    width: 4px; height: 10px;
    margin-left: -2px;
    border-left: 1px solid var(--white);
    border-right: 1px solid var(--white);
  }
  .item-desc {
    margin: 8px 0 0;
    padding-left: 6px;
    font: 400 10px/12px "Arvo", serif;
  }
  .item-price {
    margin: 6px 0 0;
    padding-left: 8px;
    font: 900 27px/30px "Lato", sans-serif;
  }
</style>
</head>
<body>
<main class="menu">
  <header>
    <div class="brand-mark">
      <p class="brand-name">Cedar<br>Hollow<br>Hampers</p>
    </div>
    <h1 class="menu-title">MENU</h1>
  </header>

  <section class="section section--cheese" aria-label="Cheese &amp; Dips"></section>
  <h2 class="section-tab section-tab--cheese">Cheese &amp; Dips</h2>

  <div class="photo photo--blue-vein" role="img" aria-label="Photo of blue vein cheese cubes with rosemary"></div>
  <article class="item" style="left:219px; top:262px; width:188px;">
    <h3 class="item-name">Blue Vein</h3>
    <div class="rule"><span class="rule-tick"></span></div>
    <p class="item-desc">Description : Lorem ipsum dolor<br>sit amet, consectetur adipiscing elit.<br>Praesent mi nisl, fringilla nec luctus<br>vel,</p>
    <p class="item-price">$9999</p>
  </article>

  <div class="photo photo--salsa" role="img" aria-label="Photo of a bowl of spicy tomato salsa with coriander"></div>
  <article class="item" style="left:629px; top:262px; width:209px;">
    <h3 class="item-name">Spicy Salsa</h3>
    <div class="rule"><span class="rule-tick"></span></div>
    <p class="item-desc">Description : Lorem ipsum dolor<br>sit amet, consectetur adipiscing elit.<br>Praesent mi nisl, fringilla nec luctus<br>vel,</p>
    <p class="item-price">$9999</p>
  </article>

  <section class="section section--crackers" aria-label="Crackers"></section>
  <h2 class="section-tab section-tab--crackers">Crackers</h2>

  <div class="photo photo--artisan" role="img" aria-label="Photo of seeded artisan crackers in a wooden bowl"></div>
  <article class="item" style="left:219px; top:566px; width:218px;">
    <h3 class="item-name item-name--stacked">Natural Artisan<br>Crackers</h3>
    <div class="rule" style="margin-top:8px;"><span class="rule-tick"></span></div>
    <p class="item-desc">Description : Lorem ipsum dolor<br>sit amet, consectetur adipiscing elit.<br>Praesent mi nisl, fringilla nec luctus</p>
    <p class="item-price">$9999</p>
  </article>

  <div class="photo photo--rice" role="img" aria-label="Photo of golden rice crackers on a plate"></div>
  <article class="item" style="left:629px; top:565px; width:209px;">
    <h3 class="item-name" style="font-size:35px;">Rice Crackers</h3>
    <div class="rule"><span class="rule-tick"></span></div>
    <p class="item-desc">Description : Lorem ipsum dolor<br>sit amet, consectetur adipiscing elit.<br>Praesent mi nisl, fringilla nec luctus<br>vel,</p>
    <p class="item-price">$9999</p>
  </article>

  <section class="section section--fruit" aria-label="Fruit"></section>
  <h2 class="section-tab section-tab--fruit">Fruit</h2>

  <div class="photo photo--strawberry" role="img" aria-label="Photo of a fresh red strawberry"></div>
  <article class="item" style="left:219px; top:855px; width:218px;">
    <h3 class="item-name">Strawberries</h3>
    <div class="rule"><span class="rule-tick"></span></div>
    <p class="item-desc">Description : Lorem ipsum dolor<br>sit amet, consectetur adipiscing elit.<br>Praesent mi nisl, fringilla nec luctus<br>vel,</p>
    <p class="item-price">$9999</p>
  </article>

  <div class="photo photo--grapes" role="img" aria-label="Photo of green grapes in a wooden bowl"></div>
  <article class="item" style="left:629px; top:855px; width:209px;">
    <h3 class="item-name item-name--centered">Grapes</h3>
    <div class="rule"><span class="rule-tick"></span></div>
    <p class="item-desc">Description : Lorem ipsum dolor<br>sit amet, consectetur adipiscing elit.<br>Praesent mi nisl, fringilla nec luctus<br>vel,</p>
    <p class="item-price">$9999</p>
  </article>

  <div class="photo photo--kiwi" role="img" aria-label="Photo of whole and halved kiwi fruit in a wicker basket"></div>
  <article class="item" style="left:417px; top:1021px; width:206px;">
    <h3 class="item-name">Kiwi Fruit</h3>
    <div class="rule"><span class="rule-tick"></span></div>
    <p class="item-desc">Description : Lorem ipsum dolor<br>sit amet, consectetur adipiscing elit.<br>Praesent mi nisl, fringilla nec luctus<br>vel,</p>
    <p class="item-price">$9999</p>
  </article>
</main>
</body>
</html>
```